Business Card Design

I used to run a Mountaineering school and am getting back into business and just want a generic type card with an adventure theme. Core activities will be mountaineering, rock climbing, canyoning, expeditions, cross country skiing,

Industry/Entity Type

School

Contact Information for Business Card

Colin Hartley Adventure Guide
email: brightfoxcolin@mailbox-example.com
+61427 836 259.

```html
<!DOCTYPE html>
<html lang="en">
<head>
<meta charset="utf-8">
<title>Colin Hartley – Adventure Guide Business Cards</title>
<link rel="stylesheet" href="https://fonts.googleapis.com/css2?family=Exo+2:wght@500;600;700&family=Ubuntu:wght@400;500&display=swap">
<style>
  :root{
    --backdrop:#f1f1f1;
    --sky:#b3dde2;
    --earth:#8b5a2b;
    --stone:#5f5a56;
    --cream:#f6e6d5;
    --navy:#3e5880;
    --white:#ffffff;
    --ink:#3d3d3d;
  }
  *{box-sizing:border-box;margin:0;padding:0}
  html,body{width:1200px;height:927px;overflow:hidden;background:var(--backdrop)}
  .canvas{position:relative;width:1200px;height:927px}
  .card{position:absolute;width:540px;height:310px;overflow:hidden;box-shadow:0 10px 24px rgba(0,0,0,.18)}
  .card--sky{left:80px;top:120px;background:var(--sky)}
  .card--navy{left:580px;top:497px;background:var(--cream)}
  .card-shapes{position:absolute;inset:0;width:540px;height:310px}
  .brand{position:absolute;right:30px;text-align:right;font-family:"Exo 2",sans-serif}
  .brand-name{font-weight:700;font-size:40px;line-height:1;letter-spacing:.5px}
  .brand-role{font-weight:500;font-size:18px;letter-spacing:6px;margin-top:4px;margin-right:-6px}
  .card--sky .brand{top:22px}
  .card--sky .brand-name{color:var(--earth)}
  .card--sky .brand-role{color:var(--ink)}
  .card--navy .brand{top:45px}
  .card--navy .brand-name,.card--navy .brand-role{color:var(--cream)}
  .services{position:absolute;list-style:none;font-family:"Ubuntu",sans-serif;text-transform:uppercase}
  .card--sky .services{right:30px;top:134px;text-align:right;color:var(--white);font-size:10.5px;line-height:15px}
  .card--navy .services{left:24px;top:28px;color:var(--navy);font-size:11px;line-height:1}
  .card--navy .services li{margin-bottom:37px}
  .contact{position:absolute;right:30px;text-align:right;font-family:"Ubuntu",sans-serif}
  .contact-line{display:flex;justify-content:flex-end;align-items:center;gap:7px}
  .contact-phone{font-family:"Exo 2",sans-serif;font-weight:700}
  .card--sky .contact{bottom:26px;color:var(--white)}
  .card--sky .contact-phone{font-size:20px;margin-bottom:10px}
  .card--sky .contact-email{font-size:12.5px}
  .card--navy .contact{bottom:26px;color:var(--white)}
  .card--navy .contact-phone{font-size:15px;margin-bottom:6px}
  .card--navy .contact-email{font-size:9.5px}
  .icon{flex:none;fill:none;stroke:currentColor;stroke-width:1.6}
</style>
</head>
<body>
<main class="canvas">

  <section class="card card--sky" aria-label="Business card, sky and earth version">
    <svg class="card-shapes" viewBox="0 0 540 310" aria-hidden="true">
      <path d="M0 200 C130 140 330 96 540 86 L540 95 C330 108 170 180 118 310 L40 310 C40 262 22 232 0 228 Z" fill="var(--stone)"/>
      <path d="M190 310 C215 200 340 112 540 100 L540 310 Z" fill="var(--earth)"/>
    </svg>
    <div class="brand">
      <h1 class="brand-name">Colin Hartley</h1>
      <p class="brand-role">ADVENTURE GUIDE</p>
    </div>
    <ul class="services">
      <li>Mountaineering</li><li>Rock Climbing</li><li>Canyoning</li><li>Expeditions</li><li>Cross Country Skiing</li>
    </ul>
    <div class="contact">
      <p class="contact-line contact-phone">+61427 836 259
        <svg class="icon" width="20" height="20" viewBox="0 0 20 20"><circle cx="10" cy="10" r="8.5"/><path d="M7 5.5 L8.6 8 L7.6 9 C8.3 10.6 9.4 11.7 11 12.4 L12 11.4 L14.5 13 L13.4 14.6 C9.5 14.2 5.8 10.5 5.4 6.6 Z" fill="currentColor" stroke="none"/></svg>
      </p>
      <p class="contact-line contact-email">email: brightfoxcolin@mailbox-example.com
        <svg class="icon" width="22" height="18" viewBox="0 0 22 18"><rect x="1" y="4" width="20" height="13"/><path d="M1 4 L11 11 L21 4 M1 17 L8.5 9.5 M21 17 L13.5 9.5 M4 4 L11 0.8 L18 4"/></svg>
      </p>
    </div>
  </section>

  <section class="card card--navy" aria-label="Business card, cream and navy version">
    <svg class="card-shapes" viewBox="0 0 540 310" aria-hidden="true">
      <path d="M205 0 C175 100 180 220 255 310 L275 310 C200 220 195 100 225 0 Z" fill="var(--navy)"/>
      <path d="M250 0 C215 110 235 230 315 310 L540 310 L540 0 Z" fill="var(--navy)"/>
    </svg>
    <ul class="services">
      <li>Mountaineering</li><li>Rock Climbing</li><li>Canyoning</li><li>Expeditions</li><li>Cross Country Skiing</li>
    </ul>
    <div class="brand">
      <h2 class="brand-name">Colin Hartley</h2>
      <p class="brand-role">ADVENTURE GUIDE</p>
    </div>
    <div class="contact">
      <p class="contact-line contact-phone">+61427 836 259
        <svg class="icon" width="16" height="16" viewBox="0 0 20 20"><circle cx="10" cy="10" r="8.5"/><path d="M7 5.5 L8.6 8 L7.6 9 C8.3 10.6 9.4 11.7 11 12.4 L12 11.4 L14.5 13 L13.4 14.6 C9.5 14.2 5.8 10.5 5.4 6.6 Z" fill="currentColor" stroke="none"/></svg>
      </p>
      <p class="contact-line contact-email">email: brightfoxcolin@mailbox-example.com
        <svg class="icon" width="17" height="14" viewBox="0 0 22 18"><rect x="1" y="4" width="20" height="13"/><path d="M1 4 L11 11 L21 4 M1 17 L8.5 9.5 M21 17 L13.5 9.5 M4 4 L11 0.8 L18 4"/></svg>
      </p>
    </div>
  </section>

</main>
</body>
</html>
```